依頼概要
■依頼の目的/概要
弊社は沖縄県にて結婚式招待状などペーパーアイテムをメインとしたウエディンググッズ通販サイトを運営しております。特徴として、沖縄発ならではのリゾートウエディング向けオリジナルペーパーアイテム商品の開発、販売を行っております。
来年に向けリゾートウエディングをコンセプトとした商品開発を行い、ラインナップをできるだけ多く増やす予定です。

■依頼詳細
女性目線の感性で「リゾートウエディング」をテーマとしたペーパーアイテムのデザインを希望します。

南国発ならではの涼しげで爽やかで開放的なリゾートをイメージできるカラーリングや、外国のガーデンウエディングのようなポップさも兼ね備えたデザインだと嬉しいです。
貴方の【カワイイ】をご提案下さい。

<モチーフ例>
魚介類、サンゴ、マーメイド、海、太陽、ハイビスカス、など。

<作っていただくもの>
●1デザイン(4アイテム)
①招待状(カバー)
②席次表
③メニュー
④席札

版下データ(PDFファイル(イラレ編集可))と見本を添付しております。
基本サイズの版下で用意しておりますが、招待状に関してはハガキサイズ(2つ折りした場合)までサイズの変更は可能です。

※基本版下は下記の商品と同じサイズになります。ご参考下さい。
<ミントリーフ>※弊社一番人気商品です。
http://www.58paper.jp/shopdetail/000000000039/invitation/page1/recommend/
<ポルカ>
http://www.58paper.jp/shopdetail/000000000219/invitation/page1/recommend/

※用紙指定や印刷加工指定(箔押し、浮き出しなど)も案があればご指定下さい。
(製造コストが合わない場合指定通りできない場合があります。)
クリスタリオなど石を付ける事もできます。

■重視する点
・赤やピンク系の色はマッチングしないため、避けてください。(定番過ぎて類似品が多いため売れにくくなっています)

■注意点
・採用者の納品されたデータ一式及び著作権は、共に弊社への譲渡となります。
全て買い取りとなりますので、ご了承下さい。
・採用の後、コストの問題で多少レイアウト等を変更して頂く場合があります。
・納品はイラストレーターデータでお願いします。

■採用デザインについて
弊社としては1点の採用だけとは制限を設けておりません。
複数の採用があれば個別にご連絡させて頂きます。

その他何かご不明な点がございましたら、お気軽にご質問下さい。
よろしくお願いいたします。
依頼公開後の追記内容
<コンペ案提出について>

・コンペのデザイン案は「招待状」のみの提出で結構です。
・採択案のみ引き続き採択デザインの展開案、他のペーパーアイテムの制作をお願いします。
・最大6~7案まで採用予定です。
招待状について
・弊社提供のデータのサイズにこだわらなくて結構です。
折った状態でハガキサイズ以内に入っていれば封筒に入りますので大丈夫です。

・比較的、淡い色調よりも派手目な色彩を好む傾向にあります。
コントラストのはっきりした、シャープな、こじんまりとしていない開放的なデザインを求めます。
<参考>
http://www.kardomart.example/invitations/coral-reef-wedding-invitations-kmi010-p-2262.html
http://www.brightgardenjournal.example/2015/05/your-wedding-style-from-start-to-finish.html
http://inkingdownsouthwithmarla.blogsite.example/2014/05/some-more-challenges.html
https://www.craftlane.example/listing/75259873/reserved-listing-for-buyer
https://www.craftlane.example/listing/196439404/custom-listing-50-wedding-thank-you
http://www.halverfern.example/wp-content/uploads/Waves-pattern-wedding-invitations.jpg
https://www.craftlane.example/listing/224828611/mermaid-invitation-birthday-mermaid
https://www.clipwall.example/pin/336433034640262054/
http://www.quillnookstudio.example/selina-t/
https://www.craftlane.example/listing/150253354/printable-bridal-shower-invitation
http://www.cardsbymirela.example/Wedding-Invitations/View-All-Wedding-Invitations/2657-White-Flourishes-Surf-Invitation
https://www.craftlane.example/listing/124067814/surfs-up-birthday-invitation-printable
http://www.papertidecrafters.example/gallery/photo/2561624
http://kvorsten7.blogsite.example/2014/08/ombre-wedding-card.html
■ 選んだ理由

全体的に弊社の要望をくみ取って下さり大変満足しております。
そんな中、恐縮ですが4点を採用とさせて頂きました。
(選定ポイント)
・弊社商品に類似していないデザイン
・弊社のイメージに近いデザイン+α
・弊社との打ち合わせ、修正依頼によって良くなる見込みのあるデザイン
・女性が好み、過去の弊社の経験から市場のニーズを感じさせるデザイン

■ 提案者全員のお礼・コメント

この度はお忙しい中弊社案件にご応募下さり、ありがとうございます。

弊社といたしましても今回限りの募集で止めること無く定期的に募集する予定でございます。

その際もご応募して頂ければ幸いです。
本当にありがとうございました。

```html
<!DOCTYPE html>
<html lang="en">
<head>
<meta charset="utf-8">
<title>Menu – Hibiscus Mint</title>
<link rel="stylesheet" href="https://fonts.googleapis.com/css2?family=Arimo&family=Pinyon+Script&display=swap">
<style>
  :root {
    --paper: #ffffff;
    --ink: #222222;
    --mint-card: #d5ecea;
    --gold: #b5a98a;
    --frame-line: #c9dcda;
    --sw-1: #d9eeee;
    --sw-2: #8fcfd3;
    --sw-3: #f2d0c4;
    --sw-4: #fbeee6;
    --sw-5: #df8a79;
    --sw-6: #7fa68a;
    --sw-7: #9fc8b4;
    --sw-8: #c7e1c4;
    --sw-9: #eef2a8;
    --sw-10: #b5a98a;
  }
  * { margin: 0; padding: 0; box-sizing: border-box; }
  html, body { width: 846px; height: 1200px; overflow: hidden; background: var(--paper); }
  .sheet { position: relative; width: 846px; height: 1200px; font-family: "Arimo", Arial, sans-serif; color: var(--ink); }
  .sheet-title { position: absolute; left: 40px; top: 34px; font-size: 20px; }
  .menu-card { position: absolute; left: 181px; top: 207px; width: 484px; height: 770px; background: var(--mint-card); }
  .menu-card__welcome { position: absolute; left: 0; right: 0; top: 18px; text-align: center; font-family: "Pinyon Script", cursive; font-size: 52px; color: var(--gold); }
  .menu-card__frame { position: absolute; left: 0; top: 0; }
  .menu-card__florals { position: absolute; left: 0; bottom: 0; }
  .palette { position: absolute; left: 85px; top: 1093px; display: flex; gap: 17px; }
  .palette__swatch { width: 34px; height: 34px; border-radius: 50%; }
  .palette__note { position: absolute; left: 636px; top: 1088px; font-size: 15px; line-height: 19px; }
  .palette__leader { position: absolute; left: 600px; top: 1110px; width: 32px; height: 1px; background: var(--ink); }
</style>
</head>
<body>
<div class="sheet">
  <p class="sheet-title">Menu [Hibiscus_MINT]</p>

  <div class="menu-card">
    <svg class="menu-card__frame" width="484" height="770" viewBox="0 0 484 770">
      <path d="M40 82 C 120 62, 190 100, 242 86 C 300 70, 370 100, 444 82 L 444 612 L 40 612 Z" fill="var(--paper)" stroke="var(--frame-line)" stroke-width="1.5"/>
    </svg>
    <p class="menu-card__welcome">Welcome</p>
    <svg class="menu-card__florals" width="484" height="260" viewBox="0 0 484 260" role="img" aria-label="Hibiscus and tropical leaf illustration along the bottom of the card">
      <defs>
        <linearGradient id="floral-tone" x1="0" y1="0" x2="1" y2="1">
          <stop offset="0" stop-color="#a9cfb9"/>
          <stop offset="0.35" stop-color="#f1d3c8"/>
          <stop offset="0.65" stop-color="#9fd3d6"/>
          <stop offset="1" stop-color="#8fb59a"/>
        </linearGradient>
      </defs>
      <path d="M12 250 L 12 70 C 12 40, 60 40, 70 60 C 90 20, 150 30, 170 60 C 200 40, 240 50, 250 80 C 280 50, 320 55, 335 75 C 360 40, 420 45, 430 65 C 450 40, 480 60, 472 90 L 472 250 Z" fill="url(#floral-tone)" opacity="0.85"/>
    </svg>
  </div>

  <div class="palette">
    <span class="palette__swatch" style="background:var(--sw-1)"></span>
    <span class="palette__swatch" style="background:var(--sw-2)"></span>
    <span class="palette__swatch" style="background:var(--sw-3)"></span>
    <span class="palette__swatch" style="background:var(--sw-4)"></span>
    <span class="palette__swatch" style="background:var(--sw-5)"></span>
    <span class="palette__swatch" style="background:var(--sw-6)"></span>
    <span class="palette__swatch" style="background:var(--sw-7)"></span>
    <span class="palette__swatch" style="background:var(--sw-8)"></span>
    <span class="palette__swatch" style="background:var(--sw-9)"></span>
    <span class="palette__swatch" style="background:var(--sw-10)"></span>
  </div>
  <span class="palette__leader"></span>
  <p class="palette__note">Light Gold Foil<br>Emboss</p>
</div>
</body>
</html>
```